Book Cover design Paws & Petals Book Cover

Please see attached brief Book title BRAVE BESIDE TAILS AND TIDES
THE QUIET GIFT OF CANINES IN LIVING AND HEALING (INCLUSIVE OF THERAPY, EDUCATION, PARENTING, CARE) I have attached a word document describing the brief. Essentially book cover should include a dog and a person, perhaps an older person and a child, and a dog, emotionally charged faces, no cartoons, happy with designer to play with concept and ideas, please avoid AI looking images.

Target Market(s)

Parents, therapists, teachers, people who work with patients/vulnerable people

Industry/Entity Type

Therapeutic care, education, non fiction

Font styles to use
Sans Serif

Requirements
Must have
• Warmth, emotion. I have included the Author photo and paragraph for the back, and also the spec in the details.

```html
<!DOCTYPE html>
<html lang="en">
<head>
<meta charset="utf-8">
<title>Brave Beside Tails and Tides – Book Cover</title>
<link href="https://fonts.googleapis.com/css2?family=Barlow:wght@400;500;700&family=Marcellus&display=swap" rel="stylesheet">
<style>
  :root{
    --stage:#949494;
    --paper:#ffffff;
    --violet:#625aa9;
    --green:#79c576;
    --pink:#f26b80;
    --teal:#22bcb5;
    --orange:#f36c4e;
    --ink:#1c1c1c;
    --fur:#c99a6a;
    --fur-light:#dcb994;
    --skin:#e3c8b8;
    --silver:#ece7e3;
  }
  html,body{margin:0;padding:0;overflow:hidden;}
  body{
    width:1200px;height:1200px;
    background:var(--stage);
    position:relative;
    font-family:"Barlow",Arial,sans-serif;
  }
  .cover{
    position:absolute;
    left:251px;top:71px;
    width:704px;height:1056px;
    background:var(--paper);
    overflow:hidden;
  }
  .cover::before{
    content:"";
    position:absolute;left:14px;top:0;bottom:0;width:3px;
    background:#eeeeee;
    z-index:3;
  }
  .cover-photo{
    position:absolute;
    left:0;top:330px;
    width:704px;height:700px;
    background:linear-gradient(115deg, var(--fur) 0%, var(--fur-light) 28%, var(--skin) 55%, var(--silver) 78%, #f7f5f3 100%);
    -webkit-mask-image:radial-gradient(ellipse 78% 72% at 52% 70%, #000 38%, transparent 100%);
    mask-image:radial-gradient(ellipse 78% 72% at 52% 70%, #000 38%, transparent 100%);
  }
  .cover-photo::after{
    content:"";
    position:absolute;inset:0;
    background:linear-gradient(to bottom, rgba(255,255,255,.9) 0%, rgba(255,255,255,0) 45%);
  }
  .title{
    position:absolute;left:72px;top:0;
    margin:0;font-weight:500;text-transform:uppercase;
    line-height:1;z-index:2;
  }
  .title .line{display:block;white-space:nowrap;position:absolute;}
  .title .line-1{font-size:166px;color:var(--violet);top:40px;letter-spacing:-1px;}
  .title .line-2{font-size:90px;top:189px;}
  .title .line-3{font-size:90px;top:270px;}
  .c-green{color:var(--green);}
  .c-pink{color:var(--pink);}
  .c-teal{color:var(--teal);}
  .c-orange{color:var(--orange);}
  .subtitle{
    position:absolute;left:70px;top:406px;
    margin:0;font-weight:400;text-transform:uppercase;
    letter-spacing:1px;line-height:1;z-index:2;
  }
  .subtitle span{display:block;white-space:nowrap;}
  .subtitle small{display:inline;}
  .subtitle .sub-1{font-size:27px;color:var(--violet);}
  .subtitle .sub-2{font-size:34px;font-weight:700;color:var(--pink);margin-top:8px;}
  .subtitle .sub-3{font-size:34px;font-weight:700;color:var(--pink);margin-top:4px;}
  .subtitle .sub-3 small{font-size:27px;font-weight:400;color:var(--violet);}
  .subtitle .sub-4{font-size:36px;color:var(--violet);margin-top:6px;}
  .subtitle .sub-4 small{font-size:27px;}
  .subtitle .sub-5{font-size:36px;color:var(--teal);margin-top:4px;}
  .author{
    position:absolute;left:0;right:0;top:962px;
    margin:0;text-align:center;z-index:2;
    font-family:"Marcellus",Georgia,serif;
    font-size:27px;letter-spacing:4px;color:var(--ink);font-weight:400;
  }
</style>
</head>
<body>
  <div class="cover">
    <div class="cover-photo" role="img" aria-label="Soft, bright photograph of an older grey-haired woman in glasses leaning her head toward a tan dog, cradling its chin in her hand"></div>

    <h1 class="title">
      <span class="line line-1">Brave</span>
      <span class="line line-2"><span class="c-green">Beside</span> <span class="c-pink">Tails</span></span>
      <span class="line line-3"><span class="c-teal">And</span> <span class="c-orange">Tides</span></span>
    </h1>

    <h2 class="subtitle">
      <span class="sub-1">The Quiet</span>
      <span class="sub-2">Gift of</span>
      <span class="sub-3">Canines <small>in</small></span>
      <span class="sub-4">Living <small>and</small></span>
      <span class="sub-5">Healing</span>
    </h2>

    <p class="author">DR HELEN MARSDEN</p>
  </div>
</body>
</html>
```